Skin care manufacturer looking for packaging design for new skin care brand.

We need a design and logo for a skin care brand to be sold at retail stores and online in the United States and Europe. The design will be for 1.7oz - 2oz serums that will not have a retail box. The name of the brand is Orvia Lune and should be a luxurious brand that is approachable. The brand will consist of 4 face serums - Vitamin C, Collagen, Retinol and Hyaluronic Acid that all contain Dead Sea Minerals. Images shown are for inspiration only. Color of bottles can be varied based on design and bottles can be screen printed or labeled.

```html
<!DOCTYPE html>
<html lang="en">
<head>
<meta charset="utf-8">
<title>Orvia Lune – Face Serum Range</title>
<link rel="stylesheet" href="https://fonts.googleapis.com/css2?family=League+Gothic&family=Montserrat:wght@300;500;700&family=Oswald:wght@500&display=swap">
<style>
  :root {
    --bg: #ececec;
    --bg-light: #f8f8f8;
    --white: #ffffff;
    --accent-yellow: #f4ef1a;
    --shell-ink: #3f4a7a;
    --bulb: #f6f6f4;

    --coral: #f07563;
    --coral-cap: #ec7b69;
    --pink: #f39bc0;
    --pink-cap: #f4b7cf;
    --red: #ee4a38;
    --red-cap: #ef5544;
    --blue: #a6bbda;
    --blue-cap: #b4c6df;
  }
  * { margin: 0; padding: 0; box-sizing: border-box; }
  html, body { width: 1200px; height: 832px; overflow: hidden; }
  body {
    background: radial-gradient(ellipse at 50% 35%, var(--bg-light) 0%, var(--bg) 70%);
    position: relative;
    font-family: "Montserrat", sans-serif;
  }

  .serum {
    position: absolute;
    top: 150px;
    width: 160px;
    height: 530px;
    margin-left: -80px;
  }
  .serum--vitamin-c { left: 192px; --body: var(--coral); --cap: var(--coral-cap); }
  .serum--collagen { left: 467px; --body: var(--pink); --cap: var(--pink-cap); }
  .serum--retinol { left: 741px; --body: var(--red); --cap: var(--red-cap); }
  .serum--hyaluronic { left: 1016px; --body: var(--blue); --cap: var(--blue-cap); }

  .dropper-bulb {
    position: absolute;
    left: 48px; top: 0;
    width: 64px; height: 100px;
    background: var(--bulb);
    border-radius: 32px 32px 4px 4px;
  }
  .collar {
    position: absolute;
    left: 23px; top: 99px;
    width: 114px; height: 93px;
    background: var(--cap);
    border-radius: 2px 2px 0 0;
  }
  .bottle-body {
    position: absolute;
    left: 0; top: 191px;
    width: 160px; height: 339px;
    background: var(--body);
    border-radius: 8px 8px 26px 26px;
    color: var(--white);
    text-align: center;
  }

  .brand-name {
    position: absolute;
    top: 32px; left: 0; right: 0;
    font-weight: 700;
    font-size: 17px;
    letter-spacing: 0.3px;
  }
  .shell-art {
    position: absolute;
    top: 96px; left: 46px;
    width: 68px; height: 36px;
  }
  .product-line {
    position: absolute;
    top: 138px; left: 0; right: 0;
    font-family: "League Gothic", sans-serif;
    font-size: 47px;
    line-height: 42px;
    letter-spacing: 0.5px;
  }
  .variant {
    position: absolute;
    top: 232px; left: 0; right: 0;
    color: var(--accent-yellow);
    font-weight: 500;
    font-size: 13px;
    line-height: 16px;
  }
  .variant--single {
    top: 236px;
    font-family: "Oswald", sans-serif;
    font-size: 16px;
  }
  .descriptor {
    position: absolute;
    top: 265px; left: 0; right: 0;
    font-family: "Oswald", sans-serif;
    font-weight: 500;
    font-size: 16px;
    line-height: 22px;
  }
  .descriptor--low { top: 269px; }
  .volume {
    position: absolute;
    top: 316px; right: 22px;
    font-weight: 300;
    font-size: 10.5px;
  }
</style>
</head>
<body>

  <div class="serum serum--vitamin-c">
    <div class="dropper-bulb"></div>
    <div class="collar"></div>
    <div class="bottle-body">
      <div class="brand-name">ORVIA LUNE</div>
      <svg class="shell-art" role="img" aria-label="Line illustration of a conch seashell" viewBox="0 0 68 36"><ellipse cx="34" cy="18" rx="34" ry="16" fill="var(--shell-ink)" opacity="0.25"/></svg>
      <div class="product-line">DEAD SEA<br>MINERALS</div>
      <div class="variant variant--single">VITAMIN C</div>
      <div class="descriptor">BRIGHTENING<br>FACE SERUM</div>
      <div class="volume">1.7oz</div>
    </div>
  </div>

  <div class="serum serum--collagen">
    <div class="dropper-bulb"></div>
    <div class="collar"></div>
    <div class="bottle-body">
      <div class="brand-name">ORVIA LUNE</div>
      <svg class="shell-art" role="img" aria-label="Line illustration of a conch seashell" viewBox="0 0 68 36"><ellipse cx="34" cy="18" rx="34" ry="16" fill="var(--shell-ink)" opacity="0.25"/></svg>
      <div class="product-line">DEAD SEA<br>MINERALS</div>
      <div class="variant">COLLAGEN<br>FIRMING</div>
      <div class="descriptor descriptor--low">BRIGHTENING<br>FACE SERUM</div>
      <div class="volume">1.7oz</div>
    </div>
  </div>

  <div class="serum serum--retinol">
    <div class="dropper-bulb"></div>
    <div class="collar"></div>
    <div class="bottle-body">
      <div class="brand-name">ORVIA LUNE</div>
      <svg class="shell-art" role="img" aria-label="Line illustration of a conch seashell" viewBox="0 0 68 36"><ellipse cx="34" cy="18" rx="34" ry="16" fill="var(--shell-ink)" opacity="0.25"/></svg>
      <div class="product-line">DEAD SEA<br>MINERALS</div>
      <div class="variant">RETINOL<br>ANTI-WRINKLE</div>
      <div class="descriptor descriptor--low">BRIGHTENING<br>FACE SERUM</div>
      <div class="volume">1.7oz</div>
    </div>
  </div>

  <div class="serum serum--hyaluronic">
    <div class="dropper-bulb"></div>
    <div class="collar"></div>
    <div class="bottle-body">
      <div class="brand-name">ORVIA LUNE</div>
      <svg class="shell-art" role="img" aria-label="Line illustration of a conch seashell" viewBox="0 0 68 36"><ellipse cx="34" cy="18" rx="34" ry="16" fill="var(--shell-ink)" opacity="0.25"/></svg>
      <div class="product-line">DEAD SEA<br>MINERALS</div>
      <div class="variant">HYALURONIC ACID<br>HYDRATING</div>
      <div class="descriptor descriptor--low">BRIGHTENING<br>FACE SERUM</div>
      <div class="volume">1.7oz</div>
    </div>
  </div>

</body>
</html>
```